Corvane Collective Web Presence Design and Relaunch

Take existing web files and "clean up" for a a more presentable web landing pad.
posted presently on a site pad CSS template. at www.corvanecollective.org

The site is clunky and unprofessional looking. Needs to be toned down so the urgency is conveyed, but not via a burning planet image.

Target Market(s)

Non-profit climate adaptation group targeting local government land management agencies, special districts and private landholders of natural resource properties.

Industry/Entity Type

Environment

Coding

Coded - Design and coding required

Number of Pages Required

4 page

Font styles to use
Serif
Sans Serif

Requirements
Must have
• Include current logos, aspects if content on current site www.corvanecollective.org
• A regional Pacific Northwest Focus (US & Canada). Content speaking to urgency but respectful of cultural diversity and norms. Sustainability themes. Emphasis on action and implementation.
Nice to have
• link to like minded projects. Appear to future generations. Diversity in thematic areas ecological resiliency, energy, food security and infrastructure.

```html
<!DOCTYPE html>
<html lang="en">
<head>
<meta charset="utf-8">
<title>Corvane Collective — Volunteers</title>
<link href="https://fonts.googleapis.com/css2?family=Montserrat:wght@400;500;600;700&family=Roboto:wght@400;500&display=swap" rel="stylesheet">
<style>
  :root {
    --white: #ffffff;
    --green: #8dc63f;
    --green-text: #8fbf4a;
    --panel: #dfe6cd;
    --overlay-top: #7c7c7c;
    --overlay-bottom: #787d6c;
    --ink: #3d3d3d;
    --nav: #555555;
    --tab: #6a6a6a;
    --scroll: #c9c9c9;
  }
  * { box-sizing: border-box; margin: 0; padding: 0; }
  html, body { width: 1200px; height: 620px; overflow: hidden; }
  body { position: relative; font-family: "Montserrat", sans-serif; background: var(--overlay-bottom); }

  .site-header { position: absolute; left: 0; top: 0; width: 1200px; height: 61px; background: var(--white); }
  .brand { position: absolute; left: 290px; top: 16px; display: flex; align-items: center; gap: 6px; }
  .brand-mark { width: 14px; height: 14px; border-radius: 50%; background: var(--green); }
  .brand-name { font-size: 15px; font-weight: 600; color: #2a8fc8; letter-spacing: .5px; line-height: 1.1; width: 70px; }
  .main-nav { position: absolute; top: 24px; font-size: 11px; letter-spacing: 1px; color: var(--nav); }
  .nav-home { left: 657px; } .nav-about { left: 712px; } .nav-contact { left: 771px; }
  .join-btn { position: absolute; left: 834px; top: 13px; width: 107px; height: 34px; background: var(--green); color: var(--white); font-weight: 700; font-size: 13px; display: flex; align-items: center; justify-content: center; letter-spacing: .3px; }

  .backdrop-top { position: absolute; left: 0; top: 61px; width: 1200px; height: 307px; background: var(--overlay-top); }

  .section-title { position: absolute; right: 613px; top: 570px; font-size: 13px; font-weight: 600; color: #2b2b2b; letter-spacing: .4px; }
  .section-text { position: absolute; right: 613px; top: 593px; width: 330px; text-align: right; font-size: 11.5px; line-height: 15px; color: #2e2e2e; }
  .section-photo { position: absolute; left: 612px; top: 553px; width: 329px; height: 67px; background: linear-gradient(180deg, #55606c, #8a96a3); }

  .modal { position: absolute; left: 180px; top: 66px; width: 839px; height: 487px; background: var(--white); }
  .modal-scroll { position: absolute; right: 4px; top: 2px; width: 5px; height: 480px; border-radius: 3px; background: var(--scroll); }
  .tabs { position: absolute; top: 60px; left: 0; width: 100%; font-family: "Roboto", sans-serif; font-size: 10px; color: var(--tab); }
  .tab { position: absolute; white-space: nowrap; }
  .tab-more { left: 259px; } .tab-why { left: 362px; } .tab-vol { left: 511px; color: var(--green-text); }

  .team-panel { position: absolute; left: 25px; top: 99px; width: 779px; height: 324px; background: var(--panel); }
  .member { position: absolute; top: 60px; width: 146px; text-align: center; }
  .member-photo { width: 146px; height: 146px; }
  .member-name { margin-top: 12px; font-size: 13px; font-weight: 600; color: var(--ink); letter-spacing: .3px; white-space: nowrap; margin-left: -30px; margin-right: -30px; }
  .member-role { margin-top: 4px; font-size: 9px; color: var(--ink); }

  .close-btn { position: absolute; left: 390px; top: 435px; width: 50px; height: 34px; border: 1px solid var(--green); color: var(--green-text); font-size: 10px; display: flex; align-items: center; justify-content: center; font-family: "Roboto", sans-serif; }
</style>
</head>
<body>
  <header class="site-header">
    <div class="brand"><span class="brand-mark"></span><span class="brand-name">Corvane Collective</span></div>
    <span class="main-nav nav-home">HOME</span>
    <span class="main-nav nav-about">ABOUT</span>
    <span class="main-nav nav-contact">CONTACT</span>
    <span class="join-btn">JOIN US</span>
  </header>

  <div class="backdrop-top"></div>

  <h2 class="section-title">ADAPTATION PLANS</h2>
  <p class="section-text">Communities throughout the region have adopted plans to to address our changing climate. Many more are in the</p>
  <div class="section-photo" role="img" aria-label="Stormy sky above a bare tree"></div>

  <div class="modal">
    <div class="modal-scroll"></div>
    <nav class="tabs">
      <span class="tab tab-more">MORE ABOUT US</span>
      <span class="tab tab-why">WHY SUPPORT OUR WORK</span>
      <span class="tab tab-vol">VOLUNTEERS</span>
    </nav>
    <section class="team-panel">
      <div class="member" style="left:60px">
        <div class="member-photo" role="img" aria-label="Portrait of volunteer Mara Olsen" style="background:linear-gradient(135deg,#c8262b,#a81e24)"></div>
        <div class="member-name">Mara Olsen</div><div class="member-role">Volunteer</div>
      </div>
      <div class="member" style="left:231px">
        <div class="member-photo" role="img" aria-label="Portrait of volunteer Tom Reese" style="background:linear-gradient(135deg,#3d5a32,#c9c2b3)"></div>
        <div class="member-name">Tom Reese</div><div class="member-role">Volunteer</div>
      </div>
      <div class="member" style="left:402px">
        <div class="member-photo" role="img" aria-label="Portrait of volunteer Walter Dunmore Jr." style="background:linear-gradient(180deg,#1f2133,#8a7060)"></div>
        <div class="member-name">Walter Dunmore Jr.</div><div class="member-role">Volunteer</div>
      </div>
      <div class="member" style="left:573px">
        <div class="member-photo" role="img" aria-label="Portrait of volunteer Kenji Marlowe" style="background:linear-gradient(135deg,#2f3a33,#9aa39c)"></div>
        <div class="member-name">Kenji Marlowe</div><div class="member-role">Volunteer</div>
      </div>
    </section>
    <span class="close-btn">Close</span>
  </div>
</body>
</html>
```